Business Card and Letterhead Design for Public Accounting Firm

Business card and letterhead design for a CPA Firm located in Orange County, CA. We're looking for a modern and professional design utilizing our existing logo. We'd like a clean "less is more" look, but also something that catches the eye. We provide a high level of service to our clients. Open to single or double sided business cards.

Additional info: color numbers on logo
Blue :
R 0
G 83
B 125

#00537D

Silver :

R 154
G 154
B 154

#9A9A9A

Target Market(s)

Businesses and individuals

Industry/Entity Type

Accounting

Contact Information for Business Card

Hewitt Dansby & Mortlake LLP - 4726 Larkspur Hollow Road, Irvine, CA 92614 - (949)382-7146 - hdmledgers.example

Font styles to use
Serif
Sans Serif
Other font styles liked:
• See font file uploaded

Colors
0054AA
0677BA
7BADD7
CADEEF
E8F1F8

Requirements
Nice to have
• Possibly use the font file provided which matches our logo, but adjust to be not in all caps

```html
<!DOCTYPE html>
<html lang="en">
<head>
<meta charset="utf-8">
<title>Hewitt Dansby &amp; Mortlake LLP — Business Card</title>
<link rel="stylesheet" href="https://fonts.googleapis.com/css2?family=Playfair+Display:wght@400&display=swap">
<style>
  :root {
    --brand-blue: #00537D;
    --accent-blue: #0054AA;
    --text-grey: #555555;
    --card-white: #ffffff;
    --backdrop: #ebe7e2;
  }
  * { margin: 0; padding: 0; box-sizing: border-box; }
  html, body {
    width: 1200px;
    height: 913px;
    overflow: hidden;
    background: var(--backdrop);
    font-family: "Playfair Display", Georgia, serif;
  }
  .canvas {
    position: relative;
    width: 1200px;
    height: 913px;
  }
  .business-card {
    position: absolute;
    left: 75px;
    top: 141px;
    width: 1050px;
    height: 630px;
    background: var(--card-white);
    box-shadow: 0 6px 24px rgba(0, 0, 0, 0.12);
  }
  .firm-name {
    position: absolute;
    left: 48px;
    top: 40px;
    display: flex;
    align-items: center;
    gap: 12px;
    color: var(--brand-blue);
    font-size: 17px;
    letter-spacing: 0.12em;
    line-height: 1.25;
    text-transform: uppercase;
  }
  .firm-mark {
    width: 14px;
    height: 14px;
    background: var(--brand-blue);
    flex: none;
  }
  .person {
    position: absolute;
    left: 0;
    right: 0;
    top: 268px;
    text-align: center;
  }
  .person-name {
    color: var(--accent-blue);
    font-size: 27px;
    letter-spacing: 0.01em;
    line-height: 1.15;
    text-transform: uppercase;
  }
  .person-title {
    color: var(--text-grey);
    font-size: 23px;
    line-height: 1.2;
  }
  .contact-item {
    position: absolute;
    top: 510px;
    transform: translateX(-50%);
    display: flex;
    flex-direction: column;
    align-items: center;
    gap: 12px;
    color: var(--text-grey);
    font-size: 18px;
    white-space: nowrap;
  }
  .contact-icon { width: 26px; height: 26px; fill: var(--accent-blue); }
  .contact-phone { left: 191px; }
  .contact-web { left: 440px; }
  .contact-address { left: 770px; }
</style>
</head>
<body>
<main class="canvas">
  <section class="business-card">
    <header class="firm-name">
      <span class="firm-mark"></span>
      <span>Hewitt Dansby<br>&amp; Mortlake LLP</span>
    </header>

    <div class="person">
      <p class="person-name">Marcus Ellery</p>
      <p class="person-title">Director</p>
    </div>

    <div class="contact-item contact-phone">
      <svg class="contact-icon" viewBox="0 0 24 24" aria-hidden="true">
        <path d="M2 9c0-3 4.5-5 10-5s10 2 10 5v1.5h-5V8.5c-1.5-.6-3.2-.9-5-.9s-3.5.3-5 .9v2H2z"/>
        <path d="M8 10h8l3 9H5z"/>
        <rect x="4" y="19" width="16" height="2"/>
      </svg>
      <span>(949)382-7146</span>
    </div>

    <div class="contact-item contact-web">
      <svg class="contact-icon" viewBox="0 0 24 24" aria-hidden="true" fill="none" stroke="#0054AA" stroke-width="1.4">
        <circle cx="12" cy="12" r="10"/>
        <ellipse cx="12" cy="12" rx="4.5" ry="10"/>
        <line x1="2" y1="12" x2="22" y2="12"/>
        <line x1="4" y1="6.5" x2="20" y2="6.5"/>
        <line x1="4" y1="17.5" x2="20" y2="17.5"/>
      </svg>
      <span>www.hdmledgers.example</span>
    </div>

    <div class="contact-item contact-address">
      <svg class="contact-icon" viewBox="0 0 24 24" aria-hidden="true">
        <path d="M12 2a7 7 0 0 0-7 7c0 5 7 13 7 13s7-8 7-13a7 7 0 0 0-7-7zm0 9.5A2.6 2.6 0 1 1 12 6.3a2.6 2.6 0 0 1 0 5.2z"/>
      </svg>
      <span>4726 Larkspur Hollow Road, Irvine, CA 92614</span>
    </div>
  </section>
</main>
</body>
</html>
```